The Lantern Guide

I am a life coach specializing in helping people with depression and bipolar disorder. I would like a nice, fun design for a business card.

```html
<!DOCTYPE html>
<html lang="en">
<head>
<meta charset="utf-8">
<title>The Lantern Guide – Business Card</title>
<link rel="stylesheet" href="https://fonts.googleapis.com/css2?family=Roboto:wght@400;500;700&display=swap">
<style>
  :root {
    --bg: #e9e7e3;
    --card: #ffffff;
    --navy: #2b4763;
    --orange: #f29a1f;
    --green: #3ea35a;
    --rule: #3f7fb8;
    --text: #4a4f57;
    --faint: #eeeeee;
  }
  * { box-sizing: border-box; margin: 0; padding: 0; }
  html, body {
    width: 900px; height: 1200px; overflow: hidden;
    background: var(--bg);
    font-family: "Roboto", Arial, sans-serif;
  }
  .card {
    position: absolute; left: 70px; width: 760px; height: 440px;
    background: var(--card); border-radius: 26px;
    box-shadow: 0 6px 18px rgba(0,0,0,.18);
    overflow: hidden;
  }
  .card--front { top: 90px; }
  .card--back { top: 660px; }

  .decor-circle {
    position: absolute; right: -40px; top: -60px;
    width: 300px; height: 300px; border-radius: 50%;
    background: var(--faint);
  }
  .brand { display: flex; align-items: center; gap: 14px; }
  .brand__dot {
    width: 64px; height: 64px; border-radius: 50%; background: var(--orange);
    flex: none;
  }
  .brand__name {
    font-weight: 500; font-size: 27px; color: var(--green);
    text-transform: uppercase; letter-spacing: .5px; white-space: nowrap;
  }
  .card--front .brand { position: absolute; left: 40px; top: 42px; }

  .person { position: absolute; left: 40px; top: 228px; }
  .person__name {
    font-weight: 700; font-size: 25px; color: var(--navy);
    text-transform: uppercase; letter-spacing: .5px;
  }
  .person__title {
    margin-top: 4px; font-weight: 500; font-size: 14px; color: var(--orange);
    text-transform: uppercase; letter-spacing: 1px;
  }
  .rule {
    position: absolute; left: 40px; right: 40px; top: 296px;
    height: 2px; background: var(--rule);
  }
  .contact {
    position: absolute; top: 318px; font-size: 15px; color: var(--text);
    line-height: 1.6;
  }
  .contact--left { left: 40px; }
  .contact--right { left: 430px; }
  .contact__row { display: flex; align-items: flex-start; gap: 10px; }
  .contact__icon { width: 14px; height: 14px; margin-top: 5px; flex: none; }

  .card--back .brand {
    position: absolute; left: 50%; top: 50%;
    transform: translate(-50%, -50%);
    flex-direction: column; gap: 18px;
  }
  .card--back .brand__dot { width: 110px; height: 110px; }
  .card--back .brand__name { font-size: 32px; }
</style>
</head>
<body>
  <section class="card card--front">
    <div class="decor-circle" aria-hidden="true"></div>
    <div class="brand">
      <span class="brand__dot" aria-hidden="true"></span>
      <span class="brand__name">The Lantern Guide</span>
    </div>
    <div class="person">
      <div class="person__name">Ray Whitcombe</div>
      <div class="person__title">Managing Director</div>
    </div>
    <div class="rule"></div>
    <div class="contact contact--left">
      <div class="contact__row">
        <svg class="contact__icon" viewBox="0 0 16 16"><path fill="#f29a1f" d="M3.6 1.2l2.2 2.6c.3.4.3.9 0 1.3L4.7 6.3a9.5 9.5 0 0 0 5 5l1.2-1.1c.4-.3.9-.3 1.3 0l2.6 2.2c.4.3.4 1 0 1.4l-1.3 1.3c-.6.6-1.6.8-2.4.4A15 15 0 0 1 .5 4.9C.1 4.1.3 3.1.9 2.5L2.2 1.2c.4-.4 1-.4 1.4 0z"/></svg>
        <span>555.014.2290</span>
      </div>
      <div class="contact__row">
        <svg class="contact__icon" viewBox="0 0 16 16"><rect x="1" y="3" width="14" height="10" rx="1.5" fill="#f29a1f"/><path d="M1.5 4l6.5 5 6.5-5" stroke="#fff" stroke-width="1.3" fill="none"/></svg>
        <span>ray@thelanternguide.com</span>
      </div>
    </div>
    <div class="contact contact--right">
      <div class="contact__row">
        <svg class="contact__icon" viewBox="0 0 16 16"><path fill="#f29a1f" d="M8 0a5.5 5.5 0 0 0-5.5 5.5C2.5 10 8 16 8 16s5.5-6 5.5-10.5A5.5 5.5 0 0 0 8 0zm0 7.8a2.3 2.3 0 1 1 0-4.6 2.3 2.3 0 0 1 0 4.6z"/></svg>
        <span>PO Box 42, Maplewood, VT 05091<br>Ray Whitcombe</span>
      </div>
    </div>
  </section>

  <section class="card card--back">
    <div class="brand">
      <span class="brand__dot" aria-hidden="true"></span>
      <span class="brand__name">The Lantern Guide</span>
    </div>
  </section>
</body>
</html>
```